Design Creative Banner or Gif Ads. 3 Designs To Be Selected

Come up with some creative banner ads for stonewell.co.nz

*At least 3 different winning banners will be chosen*

Please provide banner ads / gif ads in common google ads / website banner formats.

They can be gif or static but must stand out while still maintaining clear clean text and visuals, with a premium professional feel (please avoid clip art or anything that gives a cheap message).

Please keep in mind that these will likely be small ads so text needs to be large and if there's there a lot of text then use multiple frames/ pages as submit as a gif.

Style
Minimal & clean lines
Architectural or realistic images
Avoid cartoon styles, clipart, or anything that looks cheap

Font
Nexa or Montserrat or similar

Tone
Premium, serious, trustworthy — fits new builds

Colours
Option 1: Deep Navy (trust & quality) & lighter blues and warm grey
Option 2: Open to bright colours to help the ads stand out, such as (but not limited to) bright pink with black, yellow, fluorescent green, provided the messaging is still done professionally.
Our logo is attached (Stone Well Logo)

Display Sizes
Ad specs for file sizes should be file formats like JPEG, GIF, and PNG, with animations limited to a max of 30 seconds or less.
We will need several different ad sizes provided for each of the 3 selected winning designs.

• Medium Rectangle: 300 × 250 pixels
• Leaderboard: 728 × 90 pixels
• Desktop Banner ad image: (640x360 pixels)
• Desktop Banner ad image 2: (300x600 pixels)
• Possibly one or two other sizes

Flexibility to be creative
The ad text, words, upper/lower case, layout, colour, theme, and images can be adjusted to how you think it will look best. The follow example ads are just examples of what we are after but we are keen to see what you can create.

Recommendations at this point:
1. Avoid text heavy
2. Looking for more Gif ads
3. Imaging: if possible use real stock photo's rather than AI

Themes:

1
Building Soon? Start Here
Free Build Planning Pack:
✓ Build Cost Calculator
✓ Hidden Cost Checklist
✓ Builder Comparison Guide
Build With Confidence
Download Free

2
Before You Choose A Builder
Compare Price, Scope, Risk & Value
Avoid Costly Mistakes
Choose The Right Builder With Confidence
Download The Free Guide

3
Planning A New Build?
Avoid These Common Mistakes:
✗ Hidden Exclusions
✗ Missing Scope
✗ Unrealistic Allowances
✗ Budget Blowouts
Download The Free Guide

4
Before You Buy Land
Know what it could cost to build.
Avoid Costly Building Mistakes
Download Our Free Guides

5
Know Your Build Budget?
• Free Build Cost Calculator
• Hidden Cost Checklist
• Build Planning Tools
Calculate Costs (Download)

Target Market(s)

Landowners looking to build

Industry/Entity Type

Building

Font styles to use
Other font styles liked:
• Nexa or Montserrat or similar

Requirements
Should not have
• Avoid cartoon styles, clipart, or anything that looks cheap

```html
<!DOCTYPE html>
<html lang="en">
<head>
<meta charset="utf-8">
<title>Stone Well – Bought Land? Banner</title>
<link rel="stylesheet" href="https://fonts.googleapis.com/css2?family=Montserrat:wght@500;600;700;800&display=swap">
<style>
  :root {
    --navy: #10304d;
    --blue: #2b8fc6;
    --blue-button: #3496cc;
    --white: #ffffff;
    --sketch: #e8edf1;
  }
  * { margin: 0; padding: 0; box-sizing: border-box; }
  html, body { width: 1200px; height: 675px; overflow: hidden; background: var(--white); }
  .banner {
    position: relative;
    width: 1200px;
    height: 675px;
    background: var(--white);
    font-family: "Montserrat", Arial, sans-serif;
    overflow: hidden;
  }
  .hero-visual { position: absolute; left: 0; top: 0; width: 1200px; height: 596px; }
  .brand { position: absolute; left: 40px; top: 24px; display: flex; align-items: center; gap: 16px; }
  .brand-mark { width: 72px; height: 72px; background: var(--navy); }
  .brand-name { font-size: 48px; font-weight: 700; color: var(--navy); line-height: 1; }
  .brand-tagline {
    font-size: 12.5px; font-weight: 700; color: var(--blue);
    letter-spacing: 0.3px; margin-top: 8px; text-transform: uppercase;
  }
  .headline {
    position: absolute; left: 38px; top: 148px;
    font-weight: 800; font-size: 92px; line-height: 1.0; letter-spacing: 1px;
  }
  .headline .line-accent { color: var(--blue); display: block; }
  .headline .line-main { color: var(--navy); display: block; margin-top: 6px; }
  .subhead {
    position: absolute; left: 40px; top: 365px;
    font-size: 33px; font-weight: 700; color: var(--blue); line-height: 1.25;
  }
  .cta {
    position: absolute; left: 38px; top: 448px;
    width: 390px; height: 76px; border-radius: 12px;
    background: var(--blue-button); color: var(--white);
    display: flex; align-items: center; justify-content: center;
    font-size: 27px; font-weight: 700; letter-spacing: 0.3px;
  }
  .footer-band {
    position: absolute; left: 0; bottom: 0; width: 1200px; height: 79px;
    background: var(--navy); color: var(--white);
    display: flex; align-items: center; justify-content: center;
    font-size: 35px; font-weight: 600; padding-left: 200px;
  }
</style>
</head>
<body>
<div class="banner">
  <svg class="hero-visual" viewBox="0 0 1200 596" xmlns="http://www.w3.org/2000/svg">
    <defs>
      <linearGradient id="sketchFade" x1="0" y1="0" x2="1" y2="0">
        <stop offset="0" stop-color="#ffffff" stop-opacity="0"/>
        <stop offset="1" stop-color="#dfe6ec"/>
      </linearGradient>
      <linearGradient id="homePhoto" x1="0" y1="0" x2="0" y2="1">
        <stop offset="0" stop-color="#9ccbe9"/>
        <stop offset="0.35" stop-color="#b9c4cc"/>
        <stop offset="0.62" stop-color="#7c858d"/>
        <stop offset="0.8" stop-color="#5f8f3c"/>
        <stop offset="1" stop-color="#6fae2e"/>
      </linearGradient>
    </defs>
    <polygon points="380,150 560,60 560,553 380,553" fill="url(#sketchFade)" role="img" aria-label="Faint architectural framing sketch of a house"/>
    <polygon points="534,200 880,22 1148,170 1148,553 534,553" fill="url(#homePhoto)" role="img" aria-label="Photo of a new two-storey family home with grey garage, white trim and a green front lawn"/>
  </svg>

  <div class="brand">
    <div class="brand-mark"></div>
    <div>
      <div class="brand-name">Stone Well</div>
      <div class="brand-tagline">Compare Quotes From Trusted Builders</div>
    </div>
  </div>

  <h1 class="headline">
    <span class="line-accent">BOUGHT</span>
    <span class="line-main">LAND?</span>
  </h1>

  <p class="subhead">Understand The Steps To<br>Building Your New Home</p>

  <div class="cta">FREE BUILD ROADMAP</div>

  <div class="footer-band">Plan With Clarity. Build With Confidence.</div>
</div>
</body>
</html>
```